Bill board design For Marlowe’s Construction

Billboard Design Request
Please design the billboard to match the branding, colors, and overall feel of our website: Marlowe's Construction Website
MARLOWE’S CONSTRUCTION
CONCRETE BUILT FOR GENERATIONS
⭐ 5-Star Rated on Zorvix
Please Include:
* All three attached project photos
* Company logo(s)
* Phone Number: 555-214-7630
* Website: MarlowesConstruction.example
* Zorvix logo with 5-star rating graphic
* Chatterly logo
* Pixtoria logo
Service Area:
Kalamazoo • Battle Creek • Coldwater • Grand Rapids
Please arrange the photos and layout in whatever way creates the strongest visual impact and readability from the road. The company name, headline, phone number, and website should be highly visible at highway speeds.
The overall appearance should be clean, professional, premium, and consistent with our website branding while highlighting our reputation, craftsmanship, and quality concrete work.
People Driving By
Concrete Construction

```html
<!DOCTYPE html>
<html lang="en">
<head>
<meta charset="utf-8">
<title>Marlowe’s Construction Billboard</title>
<link rel="stylesheet" href="https://fonts.googleapis.com/css2?family=Bebas+Neue&family=Poppins:wght@500;600;700;800&display=swap">
<style>
  :root {
    --page-bg: #e4dcd9;
    --board-white: #ffffff;
    --board-black: #111214;
    --brand-blue: #1c95e6;
    --ink: #111111;
    --muted: #8a8a8a;
    --star-gold: #f5b400;
    --photo-warm: #8a6a4c;
  }
  * { margin: 0; padding: 0; box-sizing: border-box; }
  html, body { width: 890px; height: 1200px; overflow: hidden; }
  body { background: var(--page-bg); position: relative; font-family: "Poppins", sans-serif; }

  .billboard {
    position: absolute; left: 35px; top: 395px;
    width: 820px; height: 410px;
    background: var(--board-white);
    box-shadow: 0 8px 14px rgba(0,0,0,0.25);
    overflow: hidden;
  }
  .top-band { position: absolute; left: 0; top: 0; width: 100%; height: 199px; background: var(--board-black); }

  .brand-mark { position: absolute; left: 28px; top: 78px; width: 190px; display: flex; align-items: center; gap: 10px; }
  .brand-mark .mark-square { width: 22px; height: 22px; background: var(--brand-blue); flex: none; }
  .brand-mark .mark-name { font-family: "Poppins", sans-serif; font-weight: 600; font-size: 19px; line-height: 1.1; color: var(--brand-blue); }

  .photo {
    position: absolute; top: 39px; width: 176px; height: 120px;
    border: 2px solid #f2f2f2; border-radius: 10px;
  }
  .photo-crew { left: 240px; background: linear-gradient(160deg, #7d8c5c 0%, #4a4038 55%, #8c6f52 100%); }
  .photo-driveway { left: 425px; background: linear-gradient(180deg, #7f9a63 0%, #6e5a50 35%, #d6d2cc 65%, #ece9e4 100%); }
  .photo-walkway { left: 610px; background: linear-gradient(180deg, #9a8a70 0%, #6c7a4a 35%, #b0643e 70%, #c07448 100%); }

  .tagline {
    position: absolute; left: 30px; top: 179px; width: 756px; height: 47px;
    background: var(--brand-blue); border-radius: 9px;
    display: flex; align-items: center; justify-content: center;
    font-weight: 700; font-size: 24px; letter-spacing: 6px; color: #fff; white-space: nowrap;
  }

  .company-name { position: absolute; left: 30px; top: 240px; font-family: "Bebas Neue", sans-serif; line-height: 0.84; }
  .company-name .line-owner { display: block; font-size: 84px; color: var(--brand-blue); }
  .company-name .line-trade { display: block; font-size: 84px; color: var(--ink); }

  .contact { position: absolute; left: 443px; top: 244px; }
  .contact-row { display: flex; align-items: center; gap: 8px; white-space: nowrap; }
  .contact-row svg { flex: none; }
  .phone-number { font-weight: 700; font-size: 44px; line-height: 1; color: var(--ink); letter-spacing: 0.5px; }
  .website { font-weight: 600; font-size: 19px; color: var(--ink); margin-top: 6px; }

  .rating { position: absolute; left: 467px; top: 330px; display: flex; align-items: center; gap: 14px; }
  .rating-brand { display: flex; flex-direction: column; align-items: center; }
  .rating-brand .rating-name { font-weight: 600; font-size: 34px; line-height: 1; color: var(--ink); }
  .rating-brand .rating-stars { font-size: 9px; color: var(--star-gold); letter-spacing: 2px; margin-top: 4px; }
  .rating-caption { font-weight: 700; font-size: 12px; line-height: 1.3; color: var(--ink); }

  .social { position: absolute; left: 700px; top: 342px; display: flex; flex-direction: column; gap: 8px; }
  .social-item { display: flex; align-items: center; gap: 6px; font-weight: 600; font-size: 12px; color: var(--ink); }
  .social-item .social-square { width: 14px; height: 14px; border-radius: 3px; background: var(--brand-blue); }
</style>
</head>
<body>
  <div class="billboard">
    <div class="top-band"></div>

    <div class="brand-mark">
      <span class="mark-square"></span>
      <span class="mark-name">Marlowe’s Construction</span>
    </div>

    <div class="photo photo-crew" role="img" aria-label="Crew member working wet concrete with a float on a residential job site"></div>
    <div class="photo photo-driveway" role="img" aria-label="Freshly poured concrete driveway leading to a detached garage"></div>
    <div class="photo photo-walkway" role="img" aria-label="Stamped red concrete walkway in front of a house"></div>

    <div class="tagline">CONCRETE BUILT FOR GENERATIONS</div>

    <h1 class="company-name">
      <span class="line-owner">MARLOWE’S</span>
      <span class="line-trade">CONSTRUCTION</span>
    </h1>

    <div class="contact">
      <div class="contact-row">
        <svg width="22" height="22" viewBox="0 0 24 24" aria-hidden="true">
          <circle cx="12" cy="12" r="12" fill="var(--brand-blue)"/>
          <path d="M8.2 5.8l2 2.2-1.2 1.8c.8 1.9 2.3 3.4 4.2 4.2l1.8-1.2 2.2 2-1.2 2.2c-4.8-.4-8.6-4.2-9-9z" fill="#fff"/>
        </svg>
        <span class="phone-number">555-214-7630</span>
      </div>
      <div class="contact-row website">
        <svg width="14" height="14" viewBox="0 0 24 24" aria-hidden="true">
          <circle cx="12" cy="12" r="12" fill="var(--brand-blue)"/>
          <g fill="none" stroke="#fff" stroke-width="1.6">
            <circle cx="12" cy="12" r="6.5"/>
            <ellipse cx="12" cy="12" rx="2.8" ry="6.5"/>
            <path d="M5.5 12h13M6.5 8.8h11M6.5 15.2h11"/>
          </g>
        </svg>
        <span>MarlowesConstruction.example</span>
      </div>
    </div>

    <div class="rating">
      <div class="rating-brand">
        <span class="rating-name">Zorvix</span>
        <span class="rating-stars">5.0 ★★★★★</span>
      </div>
      <div class="rating-caption">5-Star<br>Rated on<br>Zorvix</div>
    </div>

    <div class="social">
      <div class="social-item"><span class="social-square"></span>Chatterly</div>
      <div class="social-item"><span class="social-square"></span>Pixtoria</div>
    </div>
  </div>
</body>
</html>
```